Building company with a modern and unique product looking for a business card to help us stand out

We currently have a logo but as our business has grown, we feel that our business card is not reflecting our modern and high quality product and help us stand out from the crowd. Our business is mainly in the construction of new homes using a unique method and materials that makes our homes fire proof, vermin and pest resistant and rated to the maximum cyclone category (category 5). We need a business card that helps us stand out as well as communicating professionalism, high quality and trustworthiness. I have attached our current logo with a black and white option, as well as our business card which is double sided. We would like to retain as much of the information that is currently on our business cards, but presented in a more sleek way. We do like our current colour palette ( white, black, yellow and grey) and have been looking primarily at business cards with a black background however we are open to other combinations of colour and layout as long as we stand out. Please feel free to tweak our logo to make it more suitable for a business card, we like the black option that we use but we have had trouble trying to get the white area to match the rest of the logo and blend effectively into a business card. Please do not hesitate to contact us with any questions as we really want this to be successful!

Target Market(s)

Large contracts including government and larger companies

Industry/Entity Type

Business

We will be providing this business card to potential clients including key government ministers and large funding companies, our business card should show that we are professional and reliable.

Requirements
Must have
• It must be easy to read and pleasing to the eye, It must contain as much of the information on the current business card and unless something really stands out, we will most likely pick a design that has all of the information included. It must include our logo of course and have some colour included.
Nice to have
• We are looking for a high end business card and would like to see designs that reflect this. We like the gloss/matte contrast, plastic cards with opaque/coloured areas and unique features not seen on everyday paper business cards. It would be nice to see a few different colour combinations, we are open to new ideas so please feel free to take some artistic licence.
Should not have
• Must not be too busy, difficult to read or be distracting from the information conveyed. Other than this please feel free to add your own touches and make it unique!

```html
<!DOCTYPE html>
<html lang="en">
<head>
<meta charset="utf-8">
<title>Ridgeline Building Company – Business Card</title>
<link rel="stylesheet" href="https://fonts.googleapis.com/css2?family=Source+Sans+3:wght@400;600;700&display=swap">
<style>
  :root {
    --stage-top: #2a2a2a;
    --stage-bottom: #050505;
    --card: #ffffff;
    --gold: #c9a227;
    --ink: #111111;
    --grey: #555555;
  }
  * { box-sizing: border-box; margin: 0; padding: 0; }
  html, body { width: 1200px; height: 900px; overflow: hidden; }
  body {
    position: relative;
    background: linear-gradient(to bottom, var(--stage-top), var(--stage-bottom));
    font-family: "Source Sans 3", "Myriad Pro", Arial, sans-serif;
    color: var(--ink);
  }
  .card {
    position: absolute;
    top: 306px;
    width: 440px;
    height: 271px;
    background: var(--card);
    border-radius: 10px;
  }
  .card--front { left: 149px; }
  .card--back { left: 608px; }

  .brand {
    position: absolute;
    left: 34px;
    top: 96px;
    width: 180px;
    display: flex;
    align-items: center;
    gap: 10px;
  }
  .brand__mark {
    flex: none;
    width: 14px;
    height: 14px;
    background: var(--gold);
  }
  .brand__name {
    font-size: 22px;
    line-height: 1.05;
    font-weight: 700;
    color: var(--ink);
  }

  .contact {
    position: absolute;
    left: 232px;
    top: 62px;
  }
  .contact__name {
    font-size: 15px;
    font-weight: 600;
    color: var(--gold);
    line-height: 18px;
  }
  .contact__role {
    font-size: 12px;
    line-height: 16px;
  }
  .contact__abn {
    margin-top: 24px;
    font-size: 12px;
    font-weight: 600;
  }
  .contact__abn span { color: var(--gold); }
  .contact__list {
    list-style: none;
    margin-top: 18px;
  }
  .contact__list li {
    display: flex;
    align-items: center;
    gap: 8px;
    font-size: 12px;
    line-height: 18px;
  }
  .contact__list svg { width: 9px; height: 9px; fill: var(--gold); flex: none; }

  .features {
    position: absolute;
    left: 227px;
    top: 101px;
  }
  .features__title {
    font-size: 13.5px;
    font-weight: 600;
    color: var(--gold);
    margin-bottom: 14px;
  }
  .features__list { list-style: none; }
  .features__list li {
    position: relative;
    padding-left: 18px;
    font-size: 12px;
    font-weight: 600;
    line-height: 18.5px;
  }
  .features__list li::before {
    content: "";
    position: absolute;
    left: 2px;
    top: 6px;
    width: 7px;
    height: 7px;
    border-radius: 50%;
    background: var(--gold);
  }
</style>
</head>
<body>
  <section class="card card--front">
    <div class="brand">
      <span class="brand__mark"></span>
      <span class="brand__name">Ridgeline Building Company</span>
    </div>
    <div class="contact">
      <p class="contact__name">Daniel Carver</p>
      <p class="contact__role">Managing Director</p>
      <p class="contact__abn"><span>ABN:</span> 48 302 615 270</p>
      <ul class="contact__list">
        <li><svg viewBox="0 0 10 10"><path d="M2 0.5 L3.6 2.6 L2.8 3.6 Q3.8 5.8 6.2 7 L7.2 6.2 L9.5 7.8 L8.4 9.5 Q3.5 9 0.5 1.6 Z"/></svg>0400 555 182</li>
        <li><svg viewBox="0 0 10 10"><rect x="1" y="3" width="8" height="6" rx="1"/><rect x="2.5" y="0.5" width="5" height="3"/></svg>(02) 55 500 417</li>
        <li><svg viewBox="0 0 10 10"><path d="M0.5 2 H9.5 V8.5 H0.5 Z M1.2 2.6 L5 5.6 L8.8 2.6" stroke="#fff" stroke-width="0.8"/></svg>ridgeline@buildmail.example</li>
      </ul>
    </div>
  </section>

  <section class="card card--back">
    <div class="brand">
      <span class="brand__mark"></span>
      <span class="brand__name">Ridgeline Building Company</span>
    </div>
    <div class="features">
      <p class="features__title">Specialising in Homes that are</p>
      <ul class="features__list">
        <li>Fire Proof</li>
        <li>Climate Proof</li>
        <li>Cyclone Rated (Cat. 5)</li>
      </ul>
    </div>
  </section>
</body>
</html>
```